Cover of Church Souvenir Book - 130th Celebration...Glenwood Harbor Fellowship Chapel

We need a dynamic church ad book cover design for our 130th Church Celebration. The book will be 80 pages of church activities and members with various ads in support of our church, so we want a standout cover design with vivid color. The three primary colors in the room during the gala will be black, blue and gold. Our logo has black and gold.

The Ad Book will be 8 1/2 x 11.

I am uploading several files that include:
1. The first is the logo.
2. The creative that was awarded 5 years ago for our 125th.
3. A picture of our church with church members at our 125th event.
Updates

Target Market(s)

Church audience. Average age is 60+

Industry/Entity Type

Faith Based

Colors

Designer to choose colors to be used in the design.

Requirements
Must have
• Eye catching design. Theme of: Celebrating the Past, Embracing the Future.
Nice to have
• Church picture of 2018 picture of church. Colors in the room will be black, gold and navy blue.

```html
<!DOCTYPE html>
<html lang="en">
<head>
<meta charset="utf-8">
<title>Glenwood Harbor Fellowship Chapel – 130 Years</title>
<link rel="stylesheet" href="https://fonts.googleapis.com/css2?family=Archivo+Black&family=Bebas+Neue&family=Montserrat:wght@600&display=swap">
<style>
  :root {
    --night: #05070f;
    --navy: #141a33;
    --gold: #e9c46c;
    --gold-deep: #a9782a;
    --gold-light: #fbe6a6;
    --white: #ffffff;
  }
  * { margin: 0; padding: 0; box-sizing: border-box; }
  html, body { width: 927px; height: 1200px; overflow: hidden; background: var(--night); }
  .cover {
    position: relative;
    width: 927px;
    height: 1200px;
    overflow: hidden;
    background: radial-gradient(circle at 50% 8%, #15192b 0%, var(--night) 45%, #0a0d1d 100%);
  }
  .backdrop { position: absolute; inset: 0; }
  .cross { position: absolute; left: 421px; top: 51px; width: 85px; height: 114px; }
  .headline {
    position: absolute;
    left: 0; width: 927px;
    top: 218px;
    text-align: center;
    font-family: "Archivo Black", sans-serif;
    font-size: 55px;
    letter-spacing: 2px;
    line-height: 1;
    white-space: nowrap;
    color: var(--gold);
    -webkit-text-stroke: 1px var(--gold-deep);
    text-shadow: 0 2px 4px rgba(0,0,0,.6);
  }
  .tagline {
    position: absolute;
    left: 0; width: 927px;
    top: 296px;
    padding-left: 18px;
    text-align: center;
    font-family: "Bebas Neue", sans-serif;
    font-size: 40px;
    letter-spacing: 18px;
    line-height: 1;
    white-space: nowrap;
    color: var(--gold);
  }
  .years-number {
    position: absolute;
    left: 0; width: 927px;
    top: 430px;
    text-align: center;
    font-family: "Bebas Neue", sans-serif;
    font-size: 332px;
    line-height: 1;
    letter-spacing: -6px;
    color: var(--white);
    transform: scaleX(0.92);
  }
  .years-label {
    position: absolute;
    left: 0; width: 927px;
    top: 722px;
    text-align: center;
    font-family: "Bebas Neue", sans-serif;
    font-size: 86px;
    line-height: 1;
    letter-spacing: -1px;
    color: var(--white);
  }
  .church-photo { position: absolute; left: 0; top: 0; width: 927px; height: 1200px; }
  .badge { position: absolute; left: 40px; top: 944px; width: 184px; height: 240px; }
  .badge-name {
    position: absolute;
    left: 72px; top: 998px;
    width: 118px;
    text-align: center;
    font-family: "Montserrat", sans-serif;
    font-weight: 600;
    font-size: 13px;
    line-height: 1.3;
    color: var(--gold);
  }
</style>
</head>
<body>
<main class="cover">
  <svg class="backdrop" viewBox="0 0 927 1200" aria-hidden="true">
    <defs>
      <radialGradient id="glow" cx="463" cy="560" r="470" gradientUnits="userSpaceOnUse">
        <stop offset="0" stop-color="#c9a04e" stop-opacity=".95"/>
        <stop offset=".35" stop-color="#8a6a2e" stop-opacity=".75"/>
        <stop offset=".7" stop-color="#2b2616" stop-opacity=".35"/>
        <stop offset="1" stop-color="#05070f" stop-opacity="0"/>
      </radialGradient>
      <radialGradient id="flare" cx=".5" cy=".5" r=".5">
        <stop offset="0" stop-color="#fffbe8"/>
        <stop offset=".25" stop-color="#f7d88a" stop-opacity=".8"/>
        <stop offset="1" stop-color="#f7d88a" stop-opacity="0"/>
      </radialGradient>
      <linearGradient id="ray" x1="0" x2="1">
        <stop offset="0" stop-color="#f7d88a" stop-opacity="0"/>
        <stop offset=".5" stop-color="#fff3c8" stop-opacity=".9"/>
        <stop offset="1" stop-color="#f7d88a" stop-opacity="0"/>
      </linearGradient>
    </defs>
    <rect width="927" height="1200" fill="url(#glow)"/>
    <circle cx="470" cy="560" r="235" fill="none" stroke="#f3d38a" stroke-opacity=".35" stroke-width="5"/>
    <circle cx="244" cy="460" r="90" fill="url(#flare)"/>
    <rect x="60" y="458" width="380" height="4" fill="url(#ray)" transform="rotate(28 244 460)"/>
    <circle cx="682" cy="875" r="80" fill="url(#flare)"/>
    <rect x="520" y="873" width="330" height="4" fill="url(#ray)" transform="rotate(-35 682 875)"/>
    <rect x="380" y="280" width="170" height="3" fill="url(#ray)"/>
    <circle cx="465" cy="281" r="6" fill="#fff7d8"/>
  </svg>

  <svg class="cross" viewBox="0 0 85 114" aria-hidden="true">
    <path d="M33 0h19v30h33v18H52v66H33V48H0V30h33z" fill="#e2bc66" stroke="#9a6d22" stroke-width="2"/>
  </svg>

  <h1 class="headline">CELEBRATING THE PAST</h1>
  <p class="tagline">EMBRACING THE FUTURE</p>
  <p class="years-number">130</p>
  <p class="years-label">YEARS</p>

  <svg class="church-photo" viewBox="0 0 927 1200">
    <defs>
      <linearGradient id="photoTone" x1="0" y1="0" x2="0" y2="1">
        <stop offset="0" stop-color="#8d5a3d" stop-opacity="0"/>
        <stop offset=".3" stop-color="#8d5a3d" stop-opacity=".85"/>
        <stop offset=".7" stop-color="#6b4a3a"/>
        <stop offset="1" stop-color="#3a3540"/>
      </linearGradient>
      <linearGradient id="swoosh" x1="0" x2="1">
        <stop offset="0" stop-color="#f8e4a0"/>
        <stop offset=".5" stop-color="#d9ad55"/>
        <stop offset="1" stop-color="#9c7128"/>
      </linearGradient>
    </defs>
    <rect role="img" aria-label="Photo of the brick church building with the congregation gathered on the lawn in front"
          x="0" y="900" width="927" height="300" fill="url(#photoTone)"/>
    <path d="M0 985 C250 1060 560 1130 927 1175 L927 1200 L0 1200 Z" fill="url(#swoosh)"/>
    <path d="M0 1020 C260 1100 580 1160 927 1190 L927 1200 L0 1200 Z" fill="#0e1226"/>
  </svg>

  <svg class="badge" viewBox="0 0 184 240" aria-hidden="true">
    <path d="M40 120 L8 222 L38 206 L58 236 L82 150 Z" fill="#d7a94e"/>
    <path d="M144 120 L176 222 L146 206 L126 236 L102 150 Z" fill="#b98a35"/>
    <circle cx="91" cy="92" r="84" fill="#0a0a0c" stroke="#d9b15b" stroke-width="9"/>
  </svg>
  <p class="badge-name">Glenwood Harbor Fellowship Chapel</p>
</main>
</body>
</html>
```